IT support company needs Banner Ad for the top of their quote layout template

We need a banner Ad for the top of our for quote layout template so it is sent out on all our quotes

The banner size must be 827 x 100 pixels - anything larger than 60 KB can cause upload time issues

We have attached our logo and examples of the quote page to see how it looks in the context of the whole page.

Essential elements of the banner
- Must have our logo but this can be changed to be different colours if it makes the design work better i.e. Tidal Grove could be all in white

Colours
- Can use all of our standard colours - Orange, Black, Grey and White

Images
- As a premium IT support company we deal with people and technology so would like to see both of these Incorporated into the banner i.e. people using technology These images could be watermarked or one colour effect.

Look and Feel
- Professional, friendly, people, technology, premium

Target Market
Small business owners and managers

Industry/Entity Type

It Company

```html
<!DOCTYPE html>
<html lang="en">
<head>
<meta charset="utf-8">
<title>Tidal Grove – Quote Banner</title>
<link rel="stylesheet" href="https://fonts.googleapis.com/css2?family=Montserrat:wght@700;800&family=Roboto:wght@400;500;700&display=swap">
<style>
  :root {
    --brand-orange: #f26a1b;
    --brand-black: #111111;
    --brand-grey: #333333;
    --brand-white: #ffffff;
    --tech-deep: #0a1f45;
    --tech-navy: #163d75;
    --tech-mid: #2f6fb0;
    --tech-light: #9fc8ee;
    --tech-glow: #e6f3ff;
  }
  * { margin: 0; padding: 0; box-sizing: border-box; }
  html, body {
    width: 1200px;
    height: 180px;
    overflow: hidden;
    background: var(--brand-white);
  }
  .banner {
    position: relative;
    width: 1200px;
    height: 180px;
    background: var(--brand-white);
    overflow: hidden;
  }
  .banner-art {
    position: absolute;
    inset: 0;
    width: 1200px;
    height: 180px;
  }
  .brand-info {
    position: absolute;
    left: 32px;
    top: 24px;
    width: 300px;
  }
  .brand-wordmark {
    font-family: "Montserrat", sans-serif;
    font-weight: 800;
    font-size: 34px;
    line-height: 36px;
    letter-spacing: 0.5px;
    color: var(--brand-black);
    white-space: nowrap;
  }
  .brand-name {
    margin-top: 16px;
    font-family: "Roboto", sans-serif;
    font-weight: 700;
    font-size: 14px;
    line-height: 16px;
    color: var(--brand-orange);
  }
  .brand-tagline {
    margin-top: 2px;
    font-family: "Roboto", sans-serif;
    font-size: 10px;
    line-height: 14.5px;
    color: var(--brand-grey);
  }
  .contact-line {
    font-family: "Roboto", sans-serif;
    font-size: 10px;
    line-height: 14px;
    color: var(--brand-grey);
  }
  .contact-phone { margin-top: 6px; }
  .contact-email { margin-top: 5px; }
  .contact-label {
    font-weight: 500;
    color: var(--brand-orange);
  }
</style>
</head>
<body>
  <div class="banner">
    <svg class="banner-art" viewBox="0 0 1200 180" xmlns="http://www.w3.org/2000/svg">
      <defs>
        <linearGradient id="techBase" x1="0" y1="0" x2="1" y2="1">
          <stop offset="0" stop-color="var(--tech-light)"/>
          <stop offset="0.4" stop-color="var(--tech-mid)"/>
          <stop offset="0.75" stop-color="var(--tech-navy)"/>
          <stop offset="1" stop-color="var(--tech-deep)"/>
        </linearGradient>
        <radialGradient id="keyGlow" cx="0.5" cy="0.5" r="0.5">
          <stop offset="0" stop-color="var(--tech-glow)" stop-opacity="0.85"/>
          <stop offset="1" stop-color="var(--tech-glow)" stop-opacity="0"/>
        </radialGradient>
        <radialGradient id="handWarm" cx="0.5" cy="0.5" r="0.5">
          <stop offset="0" stop-color="#c9a58a" stop-opacity="0.55"/>
          <stop offset="1" stop-color="#c9a58a" stop-opacity="0"/>
        </radialGradient>
        <clipPath id="photoClip">
          <path d="M420 0 C400 60 414 130 505 180 H1200 V0 Z"/>
        </clipPath>
      </defs>
      <path class="swoosh-black" d="M362 0 C346 70 370 140 440 180 H1200 V0 Z" fill="var(--brand-black)"/>
      <path class="swoosh-orange" d="M388 0 C372 66 392 136 468 180 H1200 V0 Z" fill="var(--brand-orange)"/>
      <path class="swoosh-black-inner" d="M404 0 C386 62 402 134 488 180 H1200 V0 Z" fill="var(--brand-black)"/>
      <g class="tech-photo" role="img" aria-label="Photo of a person's hand typing on a backlit laptop keyboard with glowing digital data overlay" clip-path="url(#photoClip)">
        <rect x="380" y="0" width="820" height="180" fill="url(#techBase)"/>
        <ellipse cx="560" cy="40" rx="180" ry="70" fill="url(#keyGlow)"/>
        <ellipse cx="870" cy="110" rx="150" ry="45" fill="url(#keyGlow)"/>
        <ellipse cx="1080" cy="30" rx="160" ry="60" fill="url(#handWarm)"/>
      </g>
    </svg>

    <div class="brand-info">
      <div class="brand-wordmark">TIDAL GROVE</div>
      <div class="brand-name">TIDAL GROVE</div>
      <p class="brand-tagline">Lorem Ipsum is simply dummy text of the printing and typesetting industry. Lorem Ipsum has been the industry's</p>
      <p class="contact-line contact-phone"><span class="contact-label">Phone Number:</span> 000 0000 0000</p>
      <p class="contact-line contact-email"><span class="contact-label">Email:</span> info@tidalgrove.com</p>
    </div>
  </div>
</body>
</html>
```